Private Maths Tuition Flyer based in London

I am opening up a new Maths tuition centre in North West London. The flyer will be delivered to over 8,000 homes within the immediate vicinity. The design should be suitable to be printed on an A5 sheet and read in a portrait orientation.

The flyer should include the following:

The headline statement should be "Private Maths Tuition"

Secondary headline statement is the following "GCSE, A-Levels, 11 Plus exams"

Some of service offerings/selling points are:

- Free first session
- Monthly Feedback reports
- Free support outside of sessions
- Clear Target grades
- Personalised Lesson plans
- Tangible Results

Another statement that should be featured is "Book your free session by visiting www.lernova.co.uk" or something similar to that.

"Contact Details:
020 4719 8263
enquiries@lernova.co.uk"

"Address:
Kelbridge Business and Innovation Centre
Ashvale Court
Wrenfield Road
HA4 9QD"

Attached you'll see a logo which should be included and also a map of where we are. I am open to new images for the map if you guys have any, rather than a screen shot from google maps but it should be clear to see.

I would like the content above to be displayed in a clear and concise manner that is easy to read. You have creative license on where this information should be displayed and where the images should be but on the whole it should look aesthetically pleasing on the eye.

Target Market(s)

Students, Parents. Parents who want maths tutors.

Industry/Entity Type

Tutoring

Font styles to use
Sans Serif

Requirements
Must have
• *logo*
• Private Maths Tuition
• GCSE, A-Levels, 11 Plus exams
• - Free first session
• - Monthly Feedback reports
• - Free support outside of sessions
• - Clear Target grades
• - Personalised Lesson plans
• - Tangible Results
• Book your free session by visiting www.lernova.co.uk" or something similar to that.
• Contact Details:
• 020 4719 8263
• enquiries@lernova.co.uk
• Address (*with map*):
• Kelbridge Business and Innovation Centre
• Ashvale Court
• Wrenfield Road
• HA4 9QD
Nice to have
• similar colour scheme as the logo. creative background design.

```html
<!DOCTYPE html>
<html lang="en">
<head>
<meta charset="utf-8">
<title>Lernova – Private Maths Tuition</title>
<link rel="stylesheet" href="https://fonts.googleapis.com/css2?family=Oswald:wght@400;500;600;700&family=Open+Sans:wght@400;600;700&display=swap">
<style>
  :root {
    --paper: #e9ebec;
    --paper-light: #f6f7f7;
    --ink: #111111;
    --ink-soft: #2a2a2a;
    --orange: #f07d1a;
    --yellow: #ffe01a;
    --blue: #1d4f8c;
    --band: rgba(40, 44, 48, 0.72);
    --photo-a: #b9b4ad;
    --photo-b: #d8d6d2;
    --tile-a: rgba(120, 190, 220, 0.28);
    --tile-b: rgba(150, 200, 120, 0.22);
    --map-base: #e4e1da;
    --map-green: #b9d59a;
  }
  * { margin: 0; padding: 0; box-sizing: border-box; }
  html, body { width: 847px; height: 1200px; overflow: hidden; }
  body { background: #ffffff; font-family: "Open Sans", sans-serif; }
  .flyer {
    position: relative;
    width: 847px; height: 1200px; overflow: hidden;
    background: linear-gradient(160deg, var(--paper-light) 0%, var(--paper) 55%, #dfe3e5 100%);
  }
  .flyer-texture {
    position: absolute; inset: 0;
    background:
      linear-gradient(135deg, transparent 60%, var(--tile-a) 60%, var(--tile-a) 68%, transparent 68%),
      linear-gradient(45deg, transparent 75%, var(--tile-b) 75%, var(--tile-b) 82%, transparent 82%);
  }
  .hero-photo {
    position: absolute; left: 0; top: 0; width: 620px; height: 360px;
    background: linear-gradient(100deg, var(--photo-a) 0%, var(--photo-b) 60%, rgba(233,235,236,0) 100%);
    -webkit-mask-image: linear-gradient(180deg, #000 55%, transparent 100%);
    mask-image: linear-gradient(180deg, #000 55%, transparent 100%);
  }
  .brand {
    position: absolute; right: 40px; top: 90px;
    display: flex; align-items: center; gap: 14px;
  }
  .brand-dot { width: 34px; height: 34px; border-radius: 50%; background: var(--orange); }
  .brand-name {
    font-family: "Oswald", sans-serif; font-weight: 600;
    font-size: 64px; color: var(--orange); letter-spacing: 1px;
  }
  .tagline-band {
    position: absolute; left: 0; top: 205px; width: 847px; height: 62px;
    background: var(--band);
  }
  .tagline {
    position: absolute; left: 0; width: 847px; top: 207px;
    text-align: center; font-family: "Oswald", sans-serif; font-weight: 700;
    font-size: 44px; color: var(--yellow); letter-spacing: 1px;
  }
  .headline {
    position: absolute; left: 0; width: 847px; top: 262px; text-align: center;
    font-family: "Oswald", sans-serif; font-weight: 500; font-size: 72px;
    color: var(--ink); line-height: 1; letter-spacing: 0.5px;
  }
  .subhead {
    position: absolute; left: 82px; top: 340px;
    font-family: "Oswald", sans-serif; font-weight: 500; font-size: 40px; color: var(--ink-soft);
  }
  .services-title {
    position: absolute; left: 42px; top: 395px;
    font-family: "Oswald", sans-serif; font-weight: 500; font-size: 32px; color: var(--ink);
  }
  .services {
    position: absolute; left: 42px; top: 440px; list-style: none;
    font-family: "Oswald", sans-serif; font-weight: 400; font-size: 38px;
    color: var(--ink); line-height: 46px;
  }
  .cta {
    position: absolute; left: 585px; top: 500px; width: 250px;
    transform: rotate(-5deg); text-align: center;
    font-family: "Oswald", sans-serif; font-weight: 700; font-size: 54px;
    line-height: 1.05; color: var(--orange);
    text-shadow: 2px 2px 0 #7a3a06;
  }
  .map-label {
    position: absolute; left: 450px; top: 832px;
    font-family: "Oswald", sans-serif; font-weight: 500; font-size: 28px; color: var(--ink);
  }
  .map {
    position: absolute; left: 440px; top: 872px; width: 382px; height: 240px;
    background: linear-gradient(135deg, var(--map-base) 0%, var(--map-green) 55%, var(--map-base) 100%);
    border: 3px solid #ffffff; box-shadow: 0 2px 6px rgba(0,0,0,0.25);
  }
  .website {
    position: absolute; left: 38px; top: 1010px;
    font-family: "Open Sans", sans-serif; font-weight: 700; font-size: 34px; color: var(--orange);
  }
  .details {
    position: absolute; top: 1062px; font-size: 14px; line-height: 19px; color: var(--ink-soft);
  }
  .details strong { font-weight: 700; color: var(--ink); }
  .contact { left: 40px; }
  .address { left: 236px; }
</style>
</head>
<body>
<main class="flyer">
  <div class="flyer-texture"></div>
  <div class="hero-photo" role="img" aria-label="Photo of a tutor helping a student with maths"></div>

  <div class="brand">
    <span class="brand-dot"></span>
    <span class="brand-name">Lernova</span>
  </div>

  <div class="tagline-band"></div>
  <p class="tagline">NEED A MATH TUTOR?</p>
  <h1 class="headline">PRIVATE MATHS TUITION</h1>
  <p class="subhead">GCSE, A-Levels, 11 Plus exams</p>

  <h2 class="services-title">SERVICES OFFERED:</h2>
  <ul class="services">
    <li>Free first session</li>
    <li>Monthly Feedback reports</li>
    <li>Free support outside of sessions</li>
    <li>Clear Target grades</li>
    <li>Personalised Lesson plans</li>
    <li>Tangible Results</li>
  </ul>

  <p class="cta">SCHEDULE<br>NOW!</p>

  <p class="map-label">LOCATION MAP</p>
  <div class="map" role="img" aria-label="Street map showing the Kelbridge Business and Innovation Centre location"></div>

  <p class="website">www.lernova.co.uk</p>
  <p class="details contact"><strong>Contact Details:</strong><br>020 4719 8263<br>enquiries@lernova.co.uk</p>
  <p class="details address"><strong>Address:</strong><br>Kelbridge Business and Innovation Centre<br>Ashvale Court<br>Wrenfield Road<br>HA4 9QD</p>
</main>
</body>
</html>
```